TALVERO - Booklet Cover to WOW Customers

Design the cover of a booklet that is attached to or included with our handmade/handcrafted artisan products. The overall dimensions of the booklet are 41/2"wide and 3"high. The booklet will be scored vertically for a finished size of 2 1/4"wide by 3"high. The front cover of the booklet will feature the TALVERO logo and the rear cover will feature a stamp/seal of certification and the following text below the stamp/seal:

Artisan quality and authenticity assured. 100% customer satisfaction guaranteed.

The design of the stamp/seal is a component of the overall design of the booklet. The stamp/seal will be printed (not embossed or foil-stamped).

DESIGN ELEMENTS:

Front Cover: We'd like a 4-color booklet. The TALVERO Terra Vue logo needs to pop on the front. No other text or image should be on front cover.

Back Cover: The color can carry through from the front cover, or be different.

Stamp on Back Cover: The stamp should look official and say TALVERO Certified.

Inside Covers: Notice there are inside pages to the booklet. These are not to be included in the design. However, the inside (opposite side) of the booklet can have color or design. Your choice.

String: We can only use an elastic string. However, the string color is something that can be incorporated into the design.

ATTACHED PICTURES:

* Our Logo.
* Pictures of Current Booklet. We want a more modern feel that allows the logo to be prominent on the front cover.
* Pictures of Brightwell Booklet. We also produce these, to give you a feel for a glossy print version of the same booklet.
* Pictures of booklet on products. To give you a feel for the many applications of the story card.
* Screenshot of our website. For inspiration.

Target Market(s)

Our customers, primarily in the US.

Font styles to use
Sans Serif

Requirements
Must have
• Convey the integrity behind the TALVERO and the Meridian Horizons brands.
• The back of the booklet features the TALVERO Certified Seal/Stamp which guarantees the quality and the authenticity of our artisan products for our customers
• Our logo is not to be altered.

```html
<!DOCTYPE html>
<html lang="en">
<head>
<meta charset="utf-8">
<title>TALVERO Booklet Cover</title>
<link href="https://fonts.googleapis.com/css2?family=Permanent+Marker&family=Montserrat:wght@400;600&display=swap" rel="stylesheet">
<style>
  :root {
    --page-bg: #ededed;
    --ink: #3b3b3b;
    --panel-white: #fbfbfb;
    --cord-grey: #8a8a8a;
    --fold-line: rgba(255,255,255,0.55);
    --wash-green: #8fc48a;
    --wash-blue: #7fb1cf;
    --wash-red: #c8554a;
    --wash-yellow: #e7cf6a;
    --wash-light: #e6ebe4;
  }
  html, body {
    margin: 0;
    width: 1200px;
    height: 1000px;
    overflow: hidden;
    background: var(--page-bg);
  }
  .booklet-spread {
    position: absolute;
    left: 75px;
    top: 150px;
    width: 1050px;
    height: 700px;
    display: flex;
    box-shadow: 0 12px 30px rgba(0,0,0,0.18);
  }
  .cover-wash {
    position: absolute;
    inset: 0;
    background:
      radial-gradient(ellipse at 18% 30%, var(--wash-light) 0%, transparent 45%),
      radial-gradient(ellipse at 40% 80%, var(--wash-red) 0%, transparent 35%),
      radial-gradient(ellipse at 55% 20%, var(--wash-blue) 0%, transparent 45%),
      radial-gradient(ellipse at 80% 75%, var(--wash-yellow) 0%, transparent 40%),
      linear-gradient(135deg, var(--wash-light) 0%, var(--wash-green) 45%, var(--wash-blue) 100%);
  }
  .cover-panel {
    position: relative;
    width: 525px;
    height: 700px;
  }
  .fold-line {
    position: absolute;
    left: 524px;
    top: 0;
    width: 2px;
    height: 700px;
    background: var(--fold-line);
  }
  .back-cover {
    display: flex;
    flex-direction: column;
    align-items: flex-start;
    padding: 70px 60px 0 50px;
    box-sizing: border-box;
  }
  .certified-seal {
    width: 170px;
    height: 170px;
    align-self: center;
  }
  .assurance-text {
    margin: 40px 0 0;
    font-family: "Permanent Marker", "Comic Sans MS", cursive;
    font-size: 38px;
    line-height: 1.3;
    color: var(--ink);
  }
  .seal-caption {
    position: absolute;
    left: 50px;
    bottom: 40px;
    font-family: "Montserrat", sans-serif;
    font-weight: 400;
    font-size: 14px;
    letter-spacing: 1px;
    color: var(--ink);
    opacity: 0.7;
  }
  .front-cover {
    display: flex;
    align-items: center;
    justify-content: center;
  }
  .name-panel {
    position: relative;
    display: flex;
    align-items: center;
    gap: 18px;
    padding: 40px 48px;
    background: var(--panel-white);
    box-shadow: 0 4px 14px rgba(0,0,0,0.12);
  }
  .name-mark {
    width: 26px;
    height: 26px;
    background: var(--ink);
  }
  .brand-name {
    margin: 0;
    font-family: "Montserrat", sans-serif;
    font-weight: 600;
    font-size: 56px;
    letter-spacing: 2px;
    color: var(--ink);
  }
  .elastic-cord {
    position: absolute;
    left: 0;
    top: 0;
    width: 1050px;
    height: 700px;
    pointer-events: none;
  }
</style>
</head>
<body>
  <div class="booklet-spread">
    <div class="cover-wash" role="img" aria-label="Soft watercolour wash in green, blue, red and yellow tones"></div>

    <section class="cover-panel back-cover">
      <svg class="certified-seal" viewBox="0 0 170 170" aria-label="TALVERO Certified Seal">
        <circle cx="85" cy="85" r="80" fill="rgba(255,255,255,0.55)" stroke="#3b3b3b" stroke-width="3"/>
        <circle cx="85" cy="85" r="64" fill="none" stroke="#3b3b3b" stroke-width="1.5"/>
      </svg>
      <p class="assurance-text">Artisan Quality And Authenticity Assured. 100% Customer Satisfaction Guaranteed.</p>
      <div class="seal-caption">TALVERO Certified</div>
    </section>

    <section class="cover-panel front-cover">
      <div class="name-panel">
        <div class="name-mark"></div>
        <p class="brand-name">TALVERO</p>
      </div>
    </section>

    <div class="fold-line"></div>

    <svg class="elastic-cord" viewBox="0 0 1050 700" aria-hidden="true">
      <path d="M525 0 C 505 120, 545 260, 520 380 C 500 480, 540 600, 515 660 C 508 680, 530 690, 540 676"
            fill="none" stroke="#8a8a8a" stroke-width="4" stroke-linecap="round"/>
    </svg>
  </div>
</body>
</html>
```